Body System Infographic for Disability Benefits Intake

We need an infographic for each of 11 body systems with the following information in each:
1. A brief explanation of the body system and what it does
2. The top 5 service-connected conditions for that body system (info provided separately) with images
3. The top 10 symptoms associated with a medical condition within that body system (info will be provided separately) with images
4. Short section at the bottom about how these conditions may be related to service (will provide info separately)

- [ ] Musculoskeletal Conditions
- [ ] Sensory Organs: Eyes, Ears, Skin, Taste, Smell
- [ ] Hearing Loss & Tinnitus
- [ ] Eye Conditions
- [ ] Dental & Oral Conditions
- [ ] Skin Conditions
- [ ] Infectious Diseases & Immune Disorders
- [ ] Respiratory Conditions
- [ ] Cardiovascular Conditions
- [ ] Digestive Conditions
- [ ] Genitourinary Conditions
- [ ] Gynecological Conditions
- [ ] Hemic & Lymphatic Conditions
- [ ] Endocrine Conditions
- [ ] Neurological & Convulsive Disorders
- [ ] Mental Health Conditions

Design should be clean and simple to view and understand, and font should be easy to read (many of our clients will be viewing this infographic on their phones). No cartoon images please!

Target Market(s)

disabled veterans

Industry/Entity Type

Medical, Anatomy

Font styles to use
Sans Serif

Colors
0054AA
0677BA
7BADD7
CADEEF
E8F1F8

Requirements
Must have
• image of the body system, common diagnoses, common symptoms, images to explain each
Should not have
• cartoon images

```html
<!DOCTYPE html>
<html lang="en">
<head>
<meta charset="utf-8">
<title>Body System Infographics</title>
<link rel="stylesheet" href="https://fonts.googleapis.com/css2?family=Montserrat:wght@600;700;800&family=Open+Sans:wght@400;600;700&display=swap">
<style>
:root{
  --navy:#0054AA;
  --blue:#0677BA;
  --sky:#7BADD7;
  --mist:#CADEEF;
  --ice:#E8F1F8;
  --orange-1:#FDB52A;
  --orange-2:#F38A12;
  --orange-3:#E86A0C;
  --stage-1:#1E6FBE;
  --stage-2:#0F4E99;
  --green-1:#1E9E6A;
  --green-2:#0B6E57;
  --ink:#2A3440;
  --white:#ffffff;
}
*{box-sizing:border-box;margin:0;padding:0}
html,body{width:1200px;height:2508px;overflow:hidden}
body{font-family:"Open Sans",Arial,sans-serif;color:var(--ink);position:relative;background:var(--stage-2)}
.showcase{position:absolute;left:0;top:0;width:1200px;height:1580px;
  background:radial-gradient(ellipse at 50% 40%,var(--orange-1) 0%,var(--orange-2) 55%,var(--orange-3) 100%)}
.gallery{position:absolute;left:0;top:1580px;width:1200px;height:928px;
  background:linear-gradient(180deg,var(--stage-1) 0%,var(--stage-2) 100%)}

.sheet{position:absolute;background:var(--white);box-shadow:0 8px 22px rgba(0,0,0,.28);padding:14px 18px}
.sheet--muscle{left:388px;top:32px;width:432px;height:856px}
.sheet--sensory{left:160px;top:780px;width:432px;height:792px}
.sheet--immune{left:624px;top:780px;width:424px;height:792px}

.sheet__title{font-family:Montserrat,Arial,sans-serif;font-weight:800;color:var(--white);
  background:linear-gradient(90deg,var(--navy),var(--blue));border-radius:4px;padding:7px 12px;font-size:17px;text-align:center}
.sheet--sensory .sheet__title,.sheet--immune .sheet__title{text-align:left;font-size:15px}
.sheet p,.sheet li{font-size:7.2px;line-height:1.45}
.intro{margin:9px 0}
.intro b{color:var(--navy)}
.figure{border-radius:4px}
.section-head{font-family:Montserrat,Arial,sans-serif;font-weight:700;color:var(--navy);font-size:10px;margin:10px 0 6px;border-bottom:1px solid var(--mist);padding-bottom:4px}
.condition-box{background:linear-gradient(90deg,var(--blue),var(--sky));border-radius:4px;padding:8px 12px;color:var(--white)}
.condition-box ol{padding-left:12px}
.condition-box li{font-weight:600}
.condition-box--light{background:var(--ice);color:var(--ink);border:1px solid var(--mist)}
.symptom-list{list-style:none}
.symptom-list li{padding:6px 10px;border-bottom:1px solid var(--mist);background:var(--ice)}
.symptom-list li b{color:var(--navy)}
.symptom-list--green li{background:linear-gradient(90deg,var(--green-2),var(--green-1));color:var(--white);border-bottom:1px solid rgba(255,255,255,.35)}
.symptom-list--green li b{color:var(--white)}
.symptom-list--blue li{background:linear-gradient(90deg,var(--navy),var(--blue));color:var(--white);border-bottom:1px solid rgba(255,255,255,.35)}
.symptom-list--blue li b{color:var(--white)}
.numbered{list-style:none}
.numbered li{margin-bottom:5px}
.numbered li b{color:var(--navy)}
.split{display:flex;gap:12px;align-items:center;margin:8px 0}
.split ul{list-style:none}
.split li{font-family:Montserrat,Arial,sans-serif;font-weight:700;font-size:8.5px;color:var(--navy);margin:3px 0}
.split li::before{content:"";display:inline-block;width:6px;height:6px;background:var(--blue);margin-right:5px;vertical-align:middle}

.thumb{position:absolute;width:112px;height:196px;background:var(--white);box-shadow:0 4px 10px rgba(0,0,0,.3);padding:8px}
.thumb .bar{height:10px;border-radius:2px;background:linear-gradient(90deg,var(--navy),var(--blue));margin-bottom:6px}
.thumb .line{height:3px;background:var(--mist);margin-bottom:3px}
.thumb .pic{height:58px;border-radius:3px;margin:6px 0}
.thumb .block{height:24px;border-radius:2px;background:var(--sky);margin-top:6px}
.thumb .block--dark{background:linear-gradient(90deg,var(--navy),var(--blue))}
</style>
</head>
<body>

<section class="showcase">

  <article class="sheet sheet--muscle">
    <h1 class="sheet__title">Musculoskeletal</h1>
    <p class="intro">The musculoskeletal system is made up of bones, muscles, joints, tendons and ligaments that support the body and allow it to move. It protects vital organs, stores minerals and works with the nerves to keep you upright, balanced and active throughout the day.</p>
    <div class="figure" role="img" aria-label="Anatomical front and back views of the human muscular system" style="height:280px;background:radial-gradient(ellipse at 50% 50%,#e6b0a0 0%,#c76a55 45%,#ffffff 80%)"></div>
    <h2 class="section-head">The top 5 service-connected conditions associated with this body system:</h2>
    <div class="condition-box">
      <ol>
        <li>Limitation of flexion of the knee</li>
        <li>Lumbosacral or cervical strain</li>
        <li>Degenerative arthritis of the spine</li>
        <li>Limitation of motion of the ankle</li>
        <li>Paralysis of the sciatic nerve</li>
      </ol>
    </div>
    <h2 class="section-head">The top 5 symptoms associated with this body system:</h2>
    <ul class="symptom-list">
      <li><b>1. Pain:</b> aching, burning or sharp pain in the joints, back or limbs that may worsen with activity or weather changes.</li>
      <li><b>2. Stiffness:</b> reduced flexibility, especially after rest or first thing in the morning.</li>
      <li><b>3. Limited motion:</b> trouble bending, lifting, reaching or walking without help.</li>
      <li><b>4. Swelling:</b> puffiness, warmth or tenderness around an affected joint or muscle.</li>
      <li><b>5. Weakness:</b> loss of strength or numbness that makes daily tasks harder to finish.</li>
    </ul>
  </article>

  <article class="sheet sheet--sensory">
    <h1 class="sheet__title">Sensory Organs: Eyes, Ears, Skin, Taste, Smell</h1>
    <p class="intro">Your sensory organs gather information from the world around you and send it to the brain. They help you see, hear, feel, taste and smell, keeping you safe and connected to people and places.</p>
    <ol class="numbered">
      <li><b>1. Eyes:</b> detect light and color so the brain can form clear images.</li>
      <li><b>2. Ears:</b> pick up sound and help keep your balance steady.</li>
      <li><b>3. Skin:</b> senses touch, pressure, heat, cold and pain.</li>
      <li><b>4. Tongue:</b> recognizes sweet, salty, sour and bitter tastes.</li>
      <li><b>5. Nose:</b> detects odors and adds flavor to food.</li>
    </ol>
    <div class="split">
      <div class="figure" role="img" aria-label="Circular photos of an eye, ear, skin, tongue and nose around a head" style="width:190px;height:150px;flex:none;background:radial-gradient(circle at 50% 50%,var(--sky) 0%,var(--mist) 55%,var(--ice) 100%)"></div>
      <ul>
        <li>Hearing Loss &amp; Tinnitus</li>
        <li>Eye Conditions</li>
        <li>Dental &amp; Oral Conditions</li>
        <li>Skin Conditions</li>
      </ul>
    </div>
    <h2 class="section-head">The top 5 service-connected conditions associated with this body system:</h2>
    <div class="condition-box condition-box--light">
      <ol>
        <li>Tinnitus</li>
        <li>Hearing loss</li>
        <li>Scars and skin conditions</li>
      </ol>
    </div>
    <h2 class="section-head">The top 5 symptoms associated with this body system:</h2>
    <ul class="symptom-list symptom-list--green">
      <li><b>1. Ringing in ears:</b> constant buzzing or ringing sounds.</li>
      <li><b>2. Hearing trouble:</b> muffled speech or asking others to repeat.</li>
      <li><b>3. Blurred vision:</b> difficulty reading or seeing at night.</li>
      <li><b>4. Skin changes:</b> rashes, itching, scarring or discoloration.</li>
      <li><b>5. Loss of taste or smell:</b> food seems bland or odors fade.</li>
    </ul>
  </article>

  <article class="sheet sheet--immune">
    <h1 class="sheet__title">Infectious Diseases &amp; Immune Disorders</h1>
    <p class="intro"><b>Infectious Diseases:</b> these illnesses are caused by germs such as bacteria, viruses, fungi or parasites that enter the body. Some spread between people, while others come from insects, water, food or the environment.</p>
    <p class="intro"><b>Immune Disorders:</b> the immune system defends the body against infection. When it is too weak or too active, it may fail to fight germs or attack healthy tissue, causing long-term illness.</p>
    <div class="figure" role="img" aria-label="Human figure raising a hand to block floating germs" style="height:230px;background:radial-gradient(ellipse at 40% 55%,var(--blue) 0%,var(--sky) 35%,var(--ice) 75%,#ffffff 100%)"></div>
    <h2 class="section-head">The top 5 service-connected conditions associated with this body system:</h2>
    <div class="condition-box condition-box--light">
      <ol>
        <li>Chronic fatigue syndrome</li>
        <li>Malaria</li>
        <li>Tuberculosis</li>
      </ol>
    </div>
    <h2 class="section-head">The top 5 symptoms associated with this body system:</h2>
    <ul class="symptom-list symptom-list--blue">
      <li><b>1. Fever:</b> repeated high temperature or chills.</li>
      <li><b>2. Fatigue:</b> lasting tiredness not helped by rest.</li>
      <li><b>3. Swollen glands:</b> tender lumps in neck or armpits.</li>
      <li><b>4. Frequent infections:</b> illness that keeps coming back.</li>
      <li><b>5. Joint and muscle aches:</b> pain spread across the body.</li>
    </ul>
  </article>

</section>

<section class="gallery" aria-label="Full set of body system sheets">
  <div class="thumb" style="left:80px;top:60px"><div class="bar"></div><div class="line"></div><div class="line"></div><div class="pic" role="img" aria-label="Body illustration" style="background:var(--mist)"></div><div class="block"></div><div class="block block--dark"></div></div>
  <div class="thumb" style="left:204px;top:60px"><div class="bar"></div><div class="line"></div><div class="pic" role="img" aria-label="Body illustration" style="background:#e3b3a6"></div><div class="block block--dark"></div><div class="block"></div></div>
  <div class="thumb" style="left:328px;top:60px"><div class="bar"></div><div class="line"></div><div class="line"></div><div class="pic" role="img" aria-label="Body illustration" style="background:var(--sky)"></div><div class="block"></div><div class="block"></div></div>
  <div class="thumb" style="left:452px;top:60px"><div class="bar"></div><div class="line"></div><div class="pic" role="img" aria-label="Body illustration" style="background:#d98a7a"></div><div class="block block--dark"></div><div class="block block--dark"></div></div>
  <div class="thumb" style="left:576px;top:60px"><div class="bar"></div><div class="line"></div><div class="line"></div><div class="pic" role="img" aria-label="Body illustration" style="background:var(--mist)"></div><div class="block"></div><div class="block block--dark"></div></div>
  <div class="thumb" style="left:700px;top:60px"><div class="bar"></div><div class="line"></div><div class="pic" role="img" aria-label="Body illustration" style="background:#c9a3a8"></div><div class="block"></div><div class="block"></div></div>
  <div class="thumb" style="left:824px;top:60px"><div class="bar"></div><div class="line"></div><div class="line"></div><div class="pic" role="img" aria-label="Body illustration" style="background:var(--sky)"></div><div class="block block--dark"></div><div class="block"></div></div>
  <div class="thumb" style="left:948px;top:60px"><div class="bar"></div><div class="line"></div><div class="pic" role="img" aria-label="Body illustration" style="background:var(--ice)"></div><div class="block"></div><div class="block block--dark"></div></div>

  <div class="thumb" style="left:100px;top:316px"><div class="bar"></div><div class="line"></div><div class="pic" role="img" aria-label="Body illustration" style="background:#e3b3a6"></div><div class="block block--dark"></div><div class="block"></div></div>
  <div class="thumb" style="left:236px;top:316px"><div class="bar"></div><div class="line"></div><div class="line"></div><div class="pic" role="img" aria-label="Body illustration" style="background:var(--mist)"></div><div class="block"></div><div class="block"></div></div>
  <div class="thumb" style="left:372px;top:316px"><div class="bar"></div><div class="line"></div><div class="pic" role="img" aria-label="Body illustration" style="background:var(--sky)"></div><div class="block block--dark"></div><div class="block block--dark"></div></div>
  <div class="thumb" style="left:508px;top:316px"><div class="bar"></div><div class="line"></div><div class="line"></div><div class="pic" role="img" aria-label="Brain illustration" style="background:var(--navy)"></div><div class="block"></div><div class="block"></div></div>
</section>

</body>
</html>
```